Scrum Master & Agile IT Coach Needing Business Website

Hello, my name is Brent Ellison
I am a project manger, scrum master, & agile coach. I work with IT development teams on major projects for Top 500 companies . My project management business has a website and can be found here: www.tq-steadfast.example

I have launched a new company, ALL focused on IT Agile Coaching, I am looking to have a website created for my new company - the name of the new company is: Pins and Pegs - Agile IT Coaching and Training.
I have a logo and it is provided in the materials. I like to logo; I am open to different color pallets.

The website will have a total of 7 pages; I have content for 5 of the 7 pages prepared; the other 2 pages will say under construction.

Page 1 Who am I, What I do, My Experience
Demonstrated experience and progression from Scrum Master to
Program Manager to Coach

Page 2 Pins & Pegs - Agile Team Coaching
teams working major IT projects, multiple months/years

Page 3 Coaching @ the Team Level

Page 4 Coaching @ the Program Level ; ScaleFlow ART level

Pages 5 -6 Under Construction

Page 7 Presentations, Slide Decks, Reference Materials

Mentors Nook need to have this highlighted somewhere Monthly Blog
Updates

Industry/Entity Type

IT development

Coding

Coded - Design and coding required

Number of Pages Required

5+ page

Requirements
Must have
• the website must be bold - I want those who visit to remember coming to my coaching site
Nice to have
• nice to have will be a modern / futuristic website; I work with IT developers, I want a website they will like
Should not have
• should not be stiff - it should be professional but fun

```html
<!DOCTYPE html>
<html lang="en">
<head>
<meta charset="utf-8">
<title>Pins &amp; Pegs - Agile IT Coaching and Training</title>
<link href="https://fonts.googleapis.com/css2?family=Kumbh+Sans:wght@400;500;600;700;800&display=swap" rel="stylesheet">
<style>
:root{
  --navy:#1b3f8e;
  --blue:#1f6fc9;
  --bright:#2a86e0;
  --deep:#0f2f73;
  --ink:#222;
  --line:#2f75cf;
  --footer:#15397f;
  --footer-dark:#0e2a5e;
}
*{box-sizing:border-box;margin:0;padding:0}
html,body{width:1200px;height:3151px;overflow:hidden}
body{position:relative;font-family:"Kumbh Sans",sans-serif;color:var(--ink);background:#fff}
.abs{position:absolute}

/* header */
.brand{left:99px;top:34px;display:flex;align-items:center;gap:14px}
.brand-mark{width:50px;height:50px;background:var(--navy)}
.brand-name{font-size:40px;font-weight:800;color:var(--navy);letter-spacing:-.5px}
.contact-item{display:flex;align-items:center;gap:12px;top:50px}
.contact-icon{width:36px;height:36px;background:var(--blue);display:flex;align-items:center;justify-content:center}
.contact-item b{display:block;font-size:14px;color:var(--navy);font-weight:700}
.contact-item span{font-size:14.5px;color:#333}
.social{top:55px;left:951px;display:flex;gap:12px}
.social div{width:29px;height:29px;background:#e4e4e4;display:flex;align-items:center;justify-content:center}
.nav{left:0;top:133px;width:1200px;height:50px;background:var(--blue);display:flex;align-items:center;padding-left:91px}
.nav a{color:#fff;text-decoration:none;font-size:16px;font-weight:500;padding:0 17px;height:50px;line-height:50px}
.nav a.active{background:var(--deep)}

/* hero */
.hero{left:0;top:183px;width:1200px;height:622px;background:#000;overflow:hidden}
.hero-art{right:0;top:0;width:640px;height:560px;background:radial-gradient(circle at 55% 45%,#1d5cc0 0%,#0b2a6a 35%,#020814 70%,#000 100%)}
.hero-kicker{left:99px;top:100px;font-size:41px;font-weight:800;color:var(--bright)}
.hero-title{left:99px;top:150px;font-size:43px;line-height:54px;font-weight:800;color:#fff}
.hero-text{left:99px;top:278px;width:480px;font-size:15.5px;line-height:25px;color:#fff}
.btn{display:flex;align-items:center;gap:14px;background:var(--blue);color:#fff;font-size:13px;font-weight:700;text-transform:uppercase;padding:0 16px;height:41px}
.hero-btn{left:99px;top:405px}
.hero-curve{left:0;top:665px}
.dots{left:565px;top:725px;display:flex;gap:10px}
.dots i{width:10px;height:10px;border-radius:50%;border:1.5px solid #fff;display:block}
.dots i.on{background:var(--bright);border-color:var(--bright)}

/* about */
.portrait-frame{left:99px;top:878px;width:470px;height:594px;border:5px solid var(--blue)}
.portrait{left:104px;top:813px;width:460px;height:654px;background:linear-gradient(180deg,#ffffff 0%,#e9e4df 10%,#8a6f57 55%,#4b3a2e 100%)}
.about{left:605px;top:872px;width:500px}
.eyebrow{display:flex;align-items:center;gap:12px;font-size:17px;color:#222}
.eyebrow::after{content:"";width:86px;height:1px;background:#333}
.about h1{font-size:45px;font-weight:800;color:var(--navy);margin-top:16px;line-height:50px}
.about h2{font-size:22.5px;font-weight:500;color:var(--blue);margin-top:6px}
.about p{font-size:13.6px;line-height:20.5px;margin-top:14px}
.about h3{font-size:14px;font-weight:700;color:var(--navy);margin-top:20px}
.about ul{list-style:none;font-size:13.6px;line-height:20.5px}
.about li::before{content:"• ";}
.about .url{font-size:13.6px}

/* roles */
.roles{left:0;top:1536px;width:1200px;height:482px;background:linear-gradient(180deg,#1d6cc6 0%,#1a5cb4 55%,#1f72d0 100%)}
.section-tag{display:flex;align-items:center;justify-content:center;gap:16px;font-size:17px}
.section-tag::before,.section-tag::after{content:"";width:86px;height:1px;background:currentColor}
.roles .section-tag{position:absolute;top:44px;left:0;width:1200px;color:#fff}
.roles h2{position:absolute;top:74px;left:0;width:1200px;text-align:center;font-size:47px;font-weight:800;color:#fff}
.role{width:220px;height:219px;top:180px}
.role-frame{position:absolute;left:16px;top:-18px;width:220px;height:256px;border:4px solid var(--bright)}
.role-card{position:absolute;left:0;top:0;width:220px;height:219px;background:#fff;text-align:center;padding-top:26px}
.role-num{width:72px;height:72px;border-radius:50%;background:var(--navy);margin:0 auto;color:#fff;font-size:52px;font-weight:500;line-height:74px}
.role-card h3{font-size:21px;line-height:25px;font-weight:700;color:var(--navy);margin-top:14px}

/* experience */
.exp-tag{left:0;top:2076px;width:1200px;color:#222}
.exp-title{left:0;top:2104px;width:1200px;text-align:center;font-size:50px;font-weight:800;color:var(--navy)}
.exp-card{top:2236px;width:326px;height:390px;border:2px solid var(--line);border-radius:16px;background:#fff;box-shadow:0 4px 10px rgba(0,0,0,.15);padding:58px 20px 0 26px}
.exp-icon{position:absolute;top:-44px;left:119px;width:88px;height:88px;border-radius:50%;background:var(--blue);display:flex;align-items:center;justify-content:center}
.exp-card h3{text-align:center;font-size:17px;line-height:25px;font-weight:700;color:var(--navy)}
.exp-card ul{margin-top:14px;padding-left:14px;font-size:13.6px;line-height:18px;color:#333}
.exp-btn{left:422px;top:2660px;width:356px;justify-content:center}

/* footer */
.footer-curve{left:0;top:2735px}
.footer{left:0;top:2864px;width:1200px;height:222px;background:var(--footer)}
.foot-col h4{font-size:17px;font-weight:800;color:#fff;text-transform:uppercase}
.foot-col h4::after{content:"";display:block;width:26px;height:2px;background:#fff;margin-top:10px}
.foot-links{list-style:none;margin-top:14px;font-size:13.8px;line-height:24.5px;color:#fff}
.foot-contact{margin-top:14px;font-size:13.6px;line-height:17px;color:#fff}
.foot-contact div{display:flex;gap:10px;margin-bottom:16px}
.divider{width:1px;background:rgba(255,255,255,.5);height:180px}
.foot-brand{left:770px;top:2925px;display:flex;align-items:center;gap:14px}
.foot-brand .brand-mark{background:#fff;width:54px;height:54px}
.foot-brand .brand-name{color:#fff;font-size:44px}
.copyright{left:0;top:3086px;width:1200px;height:65px;background:var(--footer-dark);color:#fff;font-size:14px;text-align:center;line-height:65px;font-weight:500}
</style>
</head>
<body>

<div class="abs brand"><div class="brand-mark"></div><div class="brand-name">Pins &amp; Pegs</div></div>
<div class="abs contact-item" style="left:500px">
  <div class="contact-icon"><svg width="18" height="18" viewBox="0 0 24 24" fill="none" stroke="#fff" stroke-width="2"><path d="M5 3h4l2 5-2.5 1.5a11 11 0 0 0 6 6L16 13l5 2v4a2 2 0 0 1-2 2A16 16 0 0 1 3 5a2 2 0 0 1 2-2z"/></svg></div>
  <div><b>Call us</b><span>(+123) 4410-7788</span></div>
</div>
<div class="abs contact-item" style="left:699px">
  <div class="contact-icon"><svg width="18" height="14" viewBox="0 0 24 18" fill="none" stroke="#fff" stroke-width="2"><rect x="1" y="1" width="22" height="16"/><path d="M1 1l11 9 11-9"/></svg></div>
  <div><b>Mail us</b><span>hello@pinspegs.example</span></div>
</div>
<div class="abs social">
  <div><svg width="14" height="14" viewBox="0 0 24 24" fill="none" stroke="#555" stroke-width="2.5"><circle cx="10" cy="10" r="7"/><path d="M15 15l7 7"/></svg></div>
  <div></div><div></div><div></div>
</div>
<nav class="abs nav">
  <a class="active">About Me</a>
  <a>Pins &amp; Pegs - Agile Team Coaching</a>
  <a>The Team Level</a>
  <a>The Program Level</a>
  <a>Why is Pins &amp; Pegs here</a>
  <a>Presentations</a>
</nav>

<section class="abs hero">
  <div class="abs hero-art" role="img" aria-label="Hand touching a glowing coaching dial with target, trophy, team and chat icons"></div>
  <div class="abs hero-kicker">PINS AND PEGS</div>
  <div class="abs hero-title">AGILE IT COACHING<br>AND TRAINING</div>
  <p class="abs hero-text">Lorem Ipsum is simply dummy text of the printing and typesetting industry. Lorem Ipsum has been the industry's standard dummy text ever since the 1500s, when an unknown printer took a galley of type and scrambled it to make.</p>
  <div class="abs btn hero-btn">Learn More <svg width="16" height="14" viewBox="0 0 16 14" fill="none" stroke="#fff" stroke-width="2"><path d="M2 1l6 6-6 6M8 1l6 6-6 6"/></svg></div>
</section>
<svg class="abs hero-curve" width="1200" height="140" viewBox="0 0 1200 140">
  <defs><linearGradient id="heroBand" x1="0" x2="1"><stop offset="0" stop-color="#0f2f73"/><stop offset=".5" stop-color="#1f6fc9"/><stop offset="1" stop-color="#0f2f73"/></linearGradient></defs>
  <path d="M0,5 Q600,200 1200,5 L1200,140 L0,140Z" fill="url(#heroBand)"/>
  <path d="M0,14 Q600,272 1200,5 L1200,140 L0,140Z" fill="#fff"/>
</svg>
<div class="abs dots"><i class="on"></i><i></i><i></i><i></i></div>

<div class="abs portrait-frame"></div>
<div class="abs portrait" role="img" aria-label="Portrait photo of Brent Ellison in a tan blazer"></div>
<section class="abs about">
  <div class="eyebrow">About Me</div>
  <h1>BRENT ELLISON</h1>
  <h2>Senior Scrum Master &amp; Team Agile Coach</h2>
  <p>Brent Ellison is the Owner of Steadfast Delivery Group, LLC and serves as Principal Lead Consultant on waterfall and agile contract opportunities. Steadfast Delivery Group, LLC has engaged on a contract basis with Top 500 companies across various industries including banking and credit unions, global supply chain, and international food distribution. Brent brings 12 years of experience to his clients encompassing various project methodologies including: waterfall, agile, and hybrid frameworks.</p>
  <h3>Coaching Designations</h3>
  <ul>
    <li>SGP-SM</li>
    <li>Certified Sprint Foundations Educator</li>
    <li>ACE-TC</li>
    <li>ScaleFlow Advanced Scrum Master</li>
    <li>A-SGP</li>
  </ul>
  <h3>Sprint Guild Profile Link</h3>
  <div class="url">https://www.sprintguild.example/profile/bellison10</div>
  <h3>Badgeway Profile Link</h3>
  <div class="url">https://www.badgeway.example/users/brent-ellison.b51f3c6d</div>
  <h3>Scaled Lean Network Profile Link</h3>
  <div class="url">https://community.scaledlean.example/profile/0071X0000093gkvRBB</div>
</section>

<section class="abs roles" role="img" aria-label="Blue-tinted photo of a team working in an office">
  <div class="section-tag">What I do</div>
  <h2>ROLES I HAVE HELD</h2>
  <div class="abs role" style="left:98px"><div class="role-frame"></div><div class="role-card"><div class="role-num">1</div><h3>Sr.<br>Scrum<br>Master</h3></div></div>
  <div class="abs role" style="left:353px"><div class="role-frame"></div><div class="role-card"><div class="role-num">2</div><h3>Advanced<br>ScaleFlow Scrum<br>Master</h3></div></div>
  <div class="abs role" style="left:609px"><div class="role-frame"></div><div class="role-card"><div class="role-num">3</div><h3>Hybrid Scrum<br>Master/ Project<br>Manager</h3></div></div>
  <div class="abs role" style="left:866px"><div class="role-frame"></div><div class="role-card"><div class="role-num">4</div><h3>Business Finance<br>Transformation<br>Program Manager</h3></div></div>
</section>

<div class="abs section-tag exp-tag">Designation</div>
<h2 class="abs exp-title">WHAT IS MY EXPERIENCE</h2>

<div class="abs exp-card" style="left:99px">
  <div class="exp-icon"><svg width="44" height="44" viewBox="0 0 44 44" fill="none" stroke="#fff" stroke-width="2.5"><circle cx="22" cy="18" r="7"/><path d="M10 38c2-8 22-8 24 0M4 22a18 18 0 0 1 32-12M40 22a18 18 0 0 1-4 11"/><path d="M36 4v6h-6"/></svg></div>
  <h3>ScaleFlow Adv Scrum<br>Master</h3>
  <ul>
    <li>Stand up teams</li>
    <li>Run development efforts concurrently leading multiple teams</li>
    <li>Run ScaleFlow ceremonies</li>
    <li>Scrum of Scrums facilitator</li>
    <li>PI Planning team facilitator (multiple teams on ART)</li>
    <li>Teach and coach to advanced development team strategies</li>
    <li>Lead program level communications and business status updates on behalf of the team</li>
  </ul>
</div>
<div class="abs exp-card" style="left:437px">
  <div class="exp-icon"><svg width="46" height="46" viewBox="0 0 46 46" fill="none" stroke="#fff" stroke-width="2.5"><circle cx="15" cy="12" r="5"/><circle cx="29" cy="12" r="5"/><path d="M5 28c1-7 19-7 20 0M19 28c1-7 19-7 20 0"/><circle cx="32" cy="34" r="6"/><path d="M32 24v4M32 40v4M22 34h4M38 34h4"/></svg></div>
  <h3>Hybrid Scrum Master /<br>Project Manger</h3>
  <ul>
    <li>Standup teams</li>
    <li>Run multiple program level projects simultaneously</li>
    <li>Implement custom hybrid development strategies</li>
    <li>Manage to project triple constraints</li>
    <li>Communications lead and business liaison</li>
    <li>Use multiple coaching styles based on team and project</li>
  </ul>
</div>
<div class="abs exp-card" style="left:776px">
  <div class="exp-icon"><svg width="44" height="44" viewBox="0 0 44 44" fill="none" stroke="#fff" stroke-width="2.5"><rect x="5" y="6" width="34" height="26"/><path d="M5 12h34M17 18l-4 4 4 4M27 18l4 4-4 4M23 17l-2 10M16 38h12M22 32v6"/></svg></div>
  <h3>Business Transformation<br>Program Manager</h3>
  <ul>
    <li>Lead business transformation efforts at the program level</li>
    <li>Work with multiple product owners, business analysts, and business stakeholders on requirements</li>
    <li>Lead the international rollout, onboarding, and support of new transformational CRM tool, Cloudledger</li>
    <li>Standup and lead multi-functional teams consisting of business and technology team members</li>
    <li>Serve as program organization and communications lead</li>
  </ul>
</div>
<div class="abs btn exp-btn">Where does coaching come in to play <svg width="16" height="14" viewBox="0 0 16 14" fill="none" stroke="#fff" stroke-width="2"><path d="M2 1l6 6-6 6M8 1l6 6-6 6"/></svg></div>

<svg class="abs footer-curve" width="1200" height="130" viewBox="0 0 1200 130">
  <defs><linearGradient id="footBand" x1="0" x2="1"><stop offset="0" stop-color="#1f6fc9"/><stop offset=".5" stop-color="#2a86e0"/><stop offset="1" stop-color="#1f6fc9"/></linearGradient></defs>
  <path d="M0,110 Q600,-90 1200,110 L1200,130 L0,130Z" fill="url(#footBand)"/>
  <path d="M0,130 Q600,-60 1200,130Z" fill="#15397f"/>
</svg>
<footer class="abs footer">
  <div class="abs foot-col" style="left:125px;top:12px">
    <h4>Quick Links</h4>
    <ul class="foot-links">
      <li>About Me</li>
      <li>Pins &amp; Pegs - Agile Team Coaching</li>
      <li>The Team Level</li>
      <li>The Program Level</li>
      <li>Why is Pins &amp; Pegs here</li>
      <li>Presentations</li>
    </ul>
  </div>
  <div class="abs divider" style="left:389px;top:5px"></div>
  <div class="abs foot-col" style="left:456px;top:12px">
    <h4>Contact Us</h4>
    <div class="foot-contact">
      <div><svg width="10" height="12" viewBox="0 0 10 14" fill="#fff"><path d="M5 0a5 5 0 0 1 5 5c0 4-5 9-5 9S0 9 0 5a5 5 0 0 1 5-5z"/></svg><span>UNIT 5678, Ground Floor, Birch Court,<br>Eastfield Office Park<br>456 Sample Avenue<br>Greenhaven</span></div>
      <div><svg width="10" height="10" viewBox="0 0 12 10" fill="#fff"><rect width="12" height="10"/></svg><span>hello@pinspegs.example</span></div>
      <div><svg width="10" height="10" viewBox="0 0 24 24" fill="#fff"><path d="M5 3h4l2 5-2.5 1.5a11 11 0 0 0 6 6L16 13l5 2v4a2 2 0 0 1-2 2A16 16 0 0 1 3 5a2 2 0 0 1 2-2z"/></svg><span>(+123) 4410-7788</span></div>
    </div>
  </div>
  <div class="abs divider" style="left:728px;top:5px"></div>
</footer>
<div class="abs foot-brand"><div class="brand-mark"></div><div class="brand-name">Pins &amp; Pegs</div></div>
<div class="abs copyright">© 2022 PINS AND PEGS - AGILE IT COACHING AND TRAINING. - ALL RIGHTS RESERVED</div>

</body>
</html>
```